Holiday Rental Company Flyer Design (DL not A5)

Note from PixelFolk Administration: The category sizing selected is A5, however the project requires DL sized artwork. Please refer to the DL template link below while the 'Special Requirements' are updated accordingly.

Project Brief:
We need a double sided DL flyer designed for an up market Holiday Rental Company that portrays a personalised approach to property management. These are to be used for letter box drops to homes we're specifically targeting so the design should be modern, complimentary colour palette, uncluttered & visually appealing.

Please Download the DL Template from Quillmark here: http://www.quillmark.com.au/qm/ns/propath/UploadResources.aspx?selectedTab=0?pfid=BFB&pf_id=BFB&xnav=easypath-upload-image#Templates

Target Market(s)

Wealthy Home Owners

Industry/Entity Type

It Company

Font styles to use
Other font styles liked:
• Avant Garde Extra Light & Demi

Colors
33b8a4

Requirements
Must have
• DL Flyer sizes (210mm width x 99mm width, plus 3mm bleed)
• Front: Logo, Main Image & Grab
• Back: Contact Details & Brief Description of our business
• Images: Ideally the main image should be the house with the pool but alternatively a lifestyle images could also be used.
Nice to have
• A creative designer!
Should not have
• Clutter & busy designs

```html
<!DOCTYPE html>
<html lang="en">
<head>
<meta charset="utf-8">
<title>Coastline Havens – DL Flyer</title>
<link rel="stylesheet" href="https://fonts.googleapis.com/css2?family=Questrial&family=Poppins:wght@500&display=swap">
<style>
  :root{
    --teal:#33b8a4;
    --teal-deep:#1fa88f;
    --pattern:#5ccbb8;
    --bg:#8fdac9;
    --white:#ffffff;
    --ink:#3d3d3d;
    --dusk-top:#2f4a6e;
    --dusk-mid:#6f8cae;
    --pool:#7fe3e6;
  }
  *{margin:0;padding:0;box-sizing:border-box}
  html,body{width:1200px;height:899px;overflow:hidden}
  body{background:var(--bg);position:relative;font-family:"Questrial",sans-serif;color:var(--ink)}

  .flyer{position:absolute;left:286px;width:630px;height:297px;background:var(--white);overflow:hidden}
  .flyer--front{top:134px}
  .flyer--back{top:467px;height:298px}

  /* front */
  .photo{position:absolute;top:0;height:100%;width:225px;
    background:linear-gradient(180deg,var(--dusk-top) 0%,var(--dusk-mid) 38%,#e9eef2 55%,var(--pool) 75%,#3fbcc4 100%)}
  .photo--left{left:0}
  .photo--right{right:0}
  .front-panel{position:absolute;left:225px;top:0;width:180px;height:100%;background:var(--white)}
  .front-pattern{position:absolute;left:225px;top:0;width:180px;height:100%;background:var(--pattern);
    clip-path:polygon(0 186px,90px 231px,180px 186px,180px 297px,0 297px)}
  .front-lines{position:absolute;inset:0}
  .brand{position:absolute;left:225px;width:180px;top:126px;text-align:center;color:var(--teal);
    font-size:22px;letter-spacing:2.5px;line-height:24px}
  .brand-mark{position:absolute;left:306px;top:190px;width:18px;height:18px;border:1.5px solid var(--teal);border-radius:50%}

  /* back */
  .back-pattern{position:absolute;inset:0;background:var(--pattern);
    clip-path:polygon(0 102px,315px 298px,630px 78px,630px 298px,0 298px)}
  .back-lines{position:absolute;inset:0}
  .back-copy{position:absolute;left:0;top:16px;width:630px;text-align:center;font-size:9.2px;line-height:11.5px}
  .back-title{font-family:"Poppins",sans-serif;font-weight:500;color:var(--teal-deep);font-size:17px;line-height:22px;margin-bottom:6px}
  .back-copy p{margin-bottom:6px}
  .back-copy .intro{width:430px;margin-left:auto;margin-right:auto}
  .back-copy .invite{color:var(--teal);width:300px;margin:8px auto 5px}
  .contact{line-height:11px}
  .contact-address{margin-bottom:5px}
</style>
</head>
<body>

<section class="flyer flyer--front" aria-label="Flyer front">
  <div class="photo photo--left" role="img" aria-label="Photo of a white holiday house with a lit pool at dusk"></div>
  <div class="photo photo--right" role="img" aria-label="Photo of a pool deck with lounge chairs beside a white house at dusk"></div>
  <div class="front-panel"></div>
  <div class="front-pattern" role="img" aria-label="Teal geometric lattice pattern"></div>

  <svg class="front-lines" viewBox="0 0 630 297" aria-hidden="true">
    <g fill="none" stroke="#ffffff" stroke-width="1.3">
      <polyline points="0,160 315,8 630,160"/>
      <polyline points="0,168 315,16 630,168"/>
      <polyline points="60,297 315,174 0,40"/>
      <polyline points="570,297 315,174 630,40"/>
    </g>
    <g fill="none" stroke="#33b8a4" stroke-width="1.2">
      <polyline points="225,52 315,8 405,52"/>
      <polyline points="225,56 315,12 405,56"/>
      <polyline points="225,60 315,16 405,60"/>
      <polyline points="225,182 315,227 405,182"/>
      <polyline points="225,178 315,223 405,178"/>
    </g>
    <defs><path id="arch" d="M230,80 Q315,-6 400,80"/></defs>
    <text font-family="Questrial, sans-serif" font-size="8.5" fill="#33b8a4" textLength="186" lengthAdjust="spacingAndGlyphs">
      <textPath href="#arch" startOffset="4" textLength="186" lengthAdjust="spacingAndGlyphs">Holiday Rental Management with a difference</textPath>
    </text>
  </svg>

  <div class="brand">COASTLINE<br>HAVENS</div>
  <div class="brand-mark"></div>
</section>

<section class="flyer flyer--back" aria-label="Flyer back">
  <div class="back-pattern" role="img" aria-label="Teal geometric lattice pattern"></div>
  <svg class="back-lines" viewBox="0 0 630 298" aria-hidden="true">
    <g fill="none" stroke="#ffffff" stroke-width="1.3">
      <polyline points="0,96 315,291 630,72"/>
      <polyline points="0,104 315,298 630,80"/>
    </g>
    <g fill="none" stroke="#33b8a4" stroke-width="1.2">
      <polyline points="0,90 315,285 630,66"/>
      <polyline points="0,85 315,280 630,61"/>
    </g>
  </svg>

  <div class="back-copy">
    <h1 class="back-title">What we do differently!</h1>
    <p class="intro">Rather than relying upon a key safe or a central pickup destination, a ‘Coastline Havens’ staff member will greet guests upon arrival.</p>
    <p class="intro">Our ‘Meet &amp; Greet’ service provides home owners with an increased level of Security and also allows us to:</p>
    <p>Prepare the home for their arrival (lights, heaters, music etc.)</p>
    <p>Establish a rapport &amp; help facilitate future bookings</p>
    <p>Reiterate their responsibilities to ensure the return of their bond</p>
    <p class="invite">If you’d like to know what your property could achieve or require additional information, please contact us on:</p>
    <div class="contact">
      <p class="contact-address">PO Box 12, Seabrook Victoria 3900</p>
      <div>e: stay@coastlinehavens.com.au</div>
      <div>w: coastlinehavens.com.au</div>
      <div>t: (03)5900 1274</div>
    </div>
  </div>
</section>

</body>
</html>
```